Business Card Project for Keel Ridge Hoisting

Business name is "Keel Ridge Hoisting" we are a scaffolding & rigging business specialising in local and remote work for:
- scaffolding (residential, commercial, industrial)
- rigging
-man material hoists
- swing stages
- labour hire

On the back of the card I would like KRH as the symbol / logo. I have attached the logos we have had created by pixel harbour. We would like to use bold colours – preferably as the same colour scheme as the logo.

Target Market(s)

Construction business

Industry/Entity Type

Construction

Contact Information for Business Card

name: Miles Fenwick
Title: Director
Phone: 0491 572 846
Address: PO BOX 4821, Ternvale SA 5197
Email: miles@keelridgehoisting.com.au
Website: www.keelridgehoisting.com.au

Font styles to use
Sans Serif

Requirements
Must have
• Must use existing logo & prefering using bold colours
Nice to have
• Would be nice to have a line of dot points in what we specialise in but not essential
• Would be nice to see some designs with a slogan but not essential
Should not have
• NA

```html
<!DOCTYPE html>
<html lang="en">
<head>
<meta charset="utf-8">
<title>Keel Ridge Hoisting – Business Card</title>
<link rel="stylesheet" href="https://fonts.googleapis.com/css2?family=Roboto:wght@400;500;700;900&display=swap">
<style>
  :root {
    --backdrop: #e9e6e2;
    --card-dark: #262424;
    --card-light: #ffffff;
    --brand-red: #e5202a;
    --ink-dark: #2a2a2a;
    --ink-grey: #5a5a5a;
    --rule-grey: #bdbdbd;
    --text-white: #ffffff;
  }
  * { box-sizing: border-box; margin: 0; padding: 0; }
  html, body {
    width: 1200px; height: 1000px; overflow: hidden;
    background: var(--backdrop);
    font-family: "Roboto", Arial, sans-serif;
  }
  .canvas { position: relative; width: 1200px; height: 1000px; }

  .card {
    position: absolute; left: 287px; width: 626px; height: 358px;
    box-shadow: 0 4px 12px rgba(0,0,0,0.25);
  }

  /* Front */
  .card--front { top: 140px; background: var(--card-dark); }
  .card--front .wordmark {
    position: absolute; left: 100px; top: 132px; width: 222px;
    text-align: center;
    font-weight: 900; font-size: 78px; line-height: 92px; letter-spacing: 2px;
    color: var(--text-white);
  }
  .card--front .divider {
    position: absolute; left: 344px; top: 122px; width: 2px; height: 114px;
    background: var(--brand-red);
  }
  .services {
    position: absolute; left: 371px; top: 116px; list-style: none;
  }
  .services li {
    position: relative; padding-left: 18px;
    font-size: 15px; line-height: 26px; color: var(--text-white);
  }
  .services li::before {
    content: ""; position: absolute; left: 0; top: 9px;
    width: 8px; height: 8px; border-radius: 50%; background: var(--brand-red);
  }

  /* Back */
  .card--back { top: 531px; background: var(--card-light); overflow: hidden; }
  .card--back .company-name {
    position: absolute; left: 36px; top: 50px;
    font-weight: 700; font-size: 30px; line-height: 40px; letter-spacing: 1px;
    color: var(--ink-dark); text-transform: uppercase;
  }
  .holder {
    position: absolute; right: 35px; top: 180px; text-align: right;
  }
  .holder .name { font-weight: 500; font-size: 18px; color: var(--brand-red); line-height: 22px; }
  .holder .title { font-size: 14px; color: var(--ink-grey); line-height: 20px; }
  .holder-rule {
    position: absolute; left: 36px; top: 212px; width: 495px; height: 1px;
    background: var(--rule-grey);
  }
  .contacts { position: absolute; left: 36px; top: 231px; list-style: none; }
  .contacts li {
    display: flex; align-items: center; gap: 8px;
    font-size: 14px; line-height: 20px; color: var(--ink-grey);
  }
  .contacts svg { width: 11px; height: 11px; flex: none; }
  .address {
    position: absolute; right: 35px; top: 256px; text-align: right;
    font-size: 14px; line-height: 18px; color: var(--ink-grey);
  }
  .card--back .base-band {
    position: absolute; left: 0; bottom: 0; width: 100%; height: 9px;
    background: var(--brand-red);
  }
</style>
</head>
<body>
<main class="canvas">

  <section class="card card--front" aria-label="Card front">
    <div class="wordmark">KRH</div>
    <div class="divider"></div>
    <ul class="services">
      <li>Scaffolding</li>
      <li>Rigging</li>
      <li>Man material hoists</li>
      <li>Swing stages</li>
      <li>Labour hire</li>
    </ul>
  </section>

  <section class="card card--back" aria-label="Card back">
    <div class="company-name">Keel Ridge Hoisting</div>

    <div class="holder">
      <p class="name">Miles Fenwick</p>
      <p class="title">Director</p>
    </div>
    <div class="holder-rule"></div>

    <ul class="contacts">
      <li>
        <svg viewBox="0 0 12 12" aria-hidden="true"><path fill="var(--brand-red)" d="M2.5 1 4.3 1 5 3.4 3.9 4.3c.6 1.5 1.8 2.7 3.3 3.3l.9-1.1L10.5 7.2V9c0 .8-.6 1.5-1.5 1.5C4.9 10.2 1.8 7.1 1.5 3 1.5 2 2 1 2.5 1z"/></svg>
        0491 572 846
      </li>
      <li>
        <svg viewBox="0 0 12 12" aria-hidden="true"><rect x="1" y="2.5" width="10" height="7" fill="var(--brand-red)"/><path d="M1 2.8 6 6.6 11 2.8" fill="none" stroke="#fff" stroke-width="1"/></svg>
        miles@keelridgehoisting.com.au
      </li>
      <li>
        <svg viewBox="0 0 12 12" aria-hidden="true"><g fill="none" stroke="var(--brand-red)" stroke-width="1.1"><circle cx="6" cy="6" r="4.8"/><ellipse cx="6" cy="6" rx="2" ry="4.8"/><path d="M1.2 6h9.6"/></g></svg>
        www.keelridgehoisting.com.au
      </li>
    </ul>

    <address class="address" style="font-style:normal">
      PO BOX 4821, Ternvale<br>SA 5197
    </address>

    <div class="base-band"></div>
  </section>

</main>
</body>
</html>
```